Mail order Nursery needs banner for promoting perennials that compliment roses.

banner should be 1135 wide x165 tall. We have an existing one displayed but we are not happy with the way it is washed out. Use your creativity to give us something that pops. Would love to see some watercolor or some other form of image other than just words washed across a stock photo. Banner needs to read Perennial Companions for Roses or some variation of that. Colors need to compliment our current theme. You can view the page and banner I want to replace at www.themeadowbellplot.com. The banner we want to replace has been uploaded to the pixel harbor file drop box. Thanks for your help and I look forward to seeing what you guys come up with. EDIT: I don't think I was clear enough in by brief. This banner promotes the sale of plants that look good planted with roses. We are getting to many submissions that are using only roses as the backdrop. We are looking for different types of plants that you would grow in your garden to compliment your roses. Thanks for all your hard work.

Target Market(s)

Home owners between 30 and 65

Industry/Entity Type

Nursery

Colors
33a6d7
e667a6

Requirements
Must have
• Text promotion perennials that compliment roses.... does not have to be those exact words but get the point across
Should not have
• Stock Photos with simple text washed across it.

```html
<!DOCTYPE html>
<html lang="en">
<head>
<meta charset="utf-8">
<title>Rose Garden Ideas – The Meadowbell Plot</title>
<link rel="stylesheet" href="https://fonts.googleapis.com/css2?family=Merriweather:ital,wght@0,300;0,400;1,300&family=Raleway:wght@400;500&family=Oswald:wght@300&display=swap">
<style>
:root{
  --blue:#33a6d7;
  --pink:#e667a6;
  --ink:#2b2b2b;
  --muted:#666;
  --soft:#8a8a8a;
  --rule:#e6e6e6;
  --bg:#ffffff;
}
*{box-sizing:border-box;margin:0;padding:0}
html,body{width:1200px;height:975px;overflow:hidden;background:var(--bg)}
body{position:relative;font-family:"Merriweather",Georgia,serif;color:var(--ink)}
.abs{position:absolute}
.top-bar{left:45px;top:197px;width:1111px;height:36px;border-bottom:1px solid var(--rule)}
.account-links{left:122px;top:10px;font-size:10px;color:#555;display:flex;gap:6px;align-items:center}
.account-links span::after{content:"•";margin-left:3px;font-size:8px}
.account-links span.last::after{content:""}
.account-links .bullet{font-size:8px}
.currency{left:435px;top:8px;font-size:9.5px;color:#555;display:flex;align-items:center;gap:4px}
.flag{width:12px;height:8px;background:linear-gradient(var(--pink) 0 50%,#fff 50% 100%);border:1px solid #bbb;position:relative}
.flag::before{content:"";position:absolute;left:0;top:0;width:5px;height:4px;background:#3a4f9a}
.search{left:767px;top:6px;width:137px;height:23px;border:1px solid #ddd;font-size:9px;color:#999;padding:5px 8px}
.search svg{position:absolute;right:6px;top:5px}
.cart-btn{left:907px;top:6px;width:23px;height:23px;background:var(--pink)}
.cart-text{left:938px;top:11px;font-size:9.5px;color:#555}
.brand{left:120px;top:256px;width:160px;text-align:center;color:var(--blue);font-size:17px;line-height:1.1;font-weight:400}
.brand small{display:block;font-size:9px;letter-spacing:1px}
.main-nav{left:413px;top:263px;display:flex;gap:25px;font-family:"Raleway",sans-serif;font-size:11px;letter-spacing:2px;color:#333}
.breadcrumb{left:162px;top:326px;font-size:10.5px;color:#333;display:flex;gap:7px;align-items:center}
.breadcrumb .current{color:var(--pink)}
.page-title{left:162px;top:351px;font-size:16px;font-weight:400;letter-spacing:.3px}
.intro{left:162px;top:390px;font-size:10px;color:#555}
.section-rule{left:162px;top:434px;width:948px;height:1px;background:#333}
.section-label{left:572px;top:428px;padding:0 10px;background:var(--bg);font-family:"Raleway",sans-serif;font-size:11px;letter-spacing:2px;color:#333}
.post-meta{left:162px;top:468px;font-size:10px;font-style:italic;font-weight:300;color:var(--soft)}
.post-title{left:162px;top:491px;font-size:10.5px;color:var(--blue);font-weight:400}
.post-excerpt{left:162px;top:511px;width:220px;font-size:10px;line-height:1.55;color:#555}
.read-more{left:162px;top:568px;font-size:10px;font-style:italic;color:#555;display:flex;gap:6px;align-items:center}
.page-rule{left:45px;top:591px;width:1111px;height:1px;background:#eee}
.promo-banner{left:159px;top:621px;width:948px;height:138px}
.promo-banner .headline{position:absolute;left:14px;top:41px;font-family:"Oswald",sans-serif;font-weight:300;font-size:32px;color:#fff;letter-spacing:1px;transform:scaleY(1.08);transform-origin:left top}
</style>
</head>
<body>

<header class="abs top-bar">
  <nav class="abs account-links">
    <i class="bullet">•</i><span>Log in</span><span>Register</span><span>My Account</span><span>Check Out</span><span class="last">Wishlist</span>
  </nav>
  <div class="abs currency">
    <svg width="9" height="9" viewBox="0 0 10 10"><circle cx="5" cy="5" r="3.2" fill="none" stroke="#555" stroke-width="2.2" stroke-dasharray="1.6 1"/><circle cx="5" cy="5" r="1" fill="#555"/></svg>
    <span class="flag"></span>USD
    <svg width="7" height="5" viewBox="0 0 7 5"><path d="M1 1l2.5 2.5L6 1" fill="none" stroke="#555"/></svg>
  </div>
  <div class="abs search">Search ...
    <svg width="11" height="11" viewBox="0 0 11 11"><circle cx="4.5" cy="4.5" r="3.3" fill="none" stroke="#222" stroke-width="1.6"/><path d="M7 7l3 3" stroke="#222" stroke-width="1.8"/></svg>
  </div>
  <div class="abs cart-btn">
    <svg width="23" height="23" viewBox="0 0 23 23"><path d="M5 6h2l2 8h7l2-6H8" fill="none" stroke="#fff" stroke-width="1.6"/><circle cx="10" cy="17" r="1.2" fill="#fff"/><circle cx="15" cy="17" r="1.2" fill="#fff"/></svg>
  </div>
  <div class="abs cart-text">Cart: 0 items - $ 0.00</div>
</header>

<div class="abs brand">The Meadowbell Plot<small>ROSE GARDEN</small></div>

<nav class="abs main-nav">
  <span>HOME</span><span>CATALOG</span><span>OUR BLOG</span><span>ABOUT US</span><span>ORDERING INFO</span><span>WISH LIST</span><span>CONTACT US</span>
</nav>

<div class="abs breadcrumb">
  <svg width="10" height="9" viewBox="0 0 10 9"><path d="M5 0L0 4.5h1.5V9h2.5V6h2v3h2.5V4.5H10z" fill="#222"/></svg>
  <span>Home</span><span>/</span><span class="current">Rose Garden Ideas</span>
</div>
<h1 class="abs page-title">ROSE GARDEN IDEAS</h1>
<p class="abs intro">INSpire ;;; &nbsp;This page is mainly pics for inspiring combo plantings - click on picture for id fo perennials.</p>

<div class="abs section-rule"></div>
<div class="abs section-label">LASTEST ADVICE</div>

<article>
  <p class="abs post-meta">November 18, 2015 / 0 comments</p>
  <h2 class="abs post-title">First Post</h2>
  <p class="abs post-excerpt">This is your store's blog. You can use it to talk about new product launches,...</p>
  <p class="abs read-more">Read more
    <svg width="12" height="6" viewBox="0 0 12 6"><path d="M0 3h10M8 1l3 2-3 2" fill="none" stroke="#333" stroke-width="1.2"/></svg>
  </p>
</article>

<div class="abs page-rule"></div>

<section class="abs promo-banner">
  <svg width="948" height="138" viewBox="0 0 948 138" role="img" aria-label="Garden scene of blue-green foliage, white daisies, yellow yarrow, pink phlox and purple allium planted as rose companions">
    <defs>
      <linearGradient id="gardenTones" x1="0" y1="0" x2="1" y2="0">
        <stop offset="0" stop-color="#33a6d7"/>
        <stop offset=".3" stop-color="#3aa2b8"/>
        <stop offset=".48" stop-color="#3f8f7a"/>
        <stop offset=".58" stop-color="#5a8a4a"/>
        <stop offset=".66" stop-color="#c9d3a8"/>
        <stop offset=".74" stop-color="#d8cf4a"/>
        <stop offset=".84" stop-color="#c04fb2"/>
        <stop offset="1" stop-color="#8a4a8e"/>
      </linearGradient>
    </defs>
    <path d="M0 0H230L264 23H948V138H800L777 122H718L688 99H0Z" fill="url(#gardenTones)"/>
  </svg>
  <div class="headline">PERENNIAL COMPANIONS FOR ROSES</div>
</section>

</body>
</html>
```